lotwise hub ad

Lotwise hub advert in Australia's leading business paper.
SIZE: 129*92
Must be bold with logo, website, email address (info@lotwisehub.com.au)

Dot points to include:
- Lotwise Hub is at the forefront of market trends
- Directly targeting the property developers and investors market
- 73% of Agencies have listed multiple properties
- Join Melbourne leading Agencies today.

Australia's ONLY dedicated portal for permit approved development sites for sale.

Include standard lotwise hub colours, be creative but bold and clear.

Refer to attachments for inspiration

Thank you
Updates

Hello, we like this design and would like to choose it however can you please complete the following changes immediately as we need to submit content to the newspaper. Remove all current content: Lotwise Hub is at the forefront.... Directly targeting the ....... 73% of Agencies have....... JOIN Melbourne leading.... info@lotwisehub email on the side AND replace with Australia's ONLY dedicated portal for listing Permit Approved Development sites for sale Directly targeting Property Developers and Investors For more information call (03) 9481 2207 or email info@lotwisehub.com.au Your immediate response would be greatly appreciated. Any issues please email me at dale@lotwisehub.com.au Thank you,

Target Market(s)

Real Estate Agents
Property Develops & Investors

Industry/Entity Type

Real Estate Agent

Font styles to use
Serif
Sans Serif

Requirements
Must have
• Refer Project description
Nice to have

```html
<!DOCTYPE html>
<html lang="en">
<head>
<meta charset="utf-8">
<title>Lotwise Hub – Newspaper Advert</title>
<link rel="stylesheet" href="https://fonts.googleapis.com/css2?family=Montserrat:wght@400;700&family=Nunito+Sans:wght@800;900&family=Merriweather:wght@400;700&display=swap">
<style>
  :root {
    --brand-crimson: #c0185a;
    --brand-grey: #a0a0a0;
    --band-yellow: #fdd000;
    --ink: #2b2b2b;
    --panel-grey: #939598;
    --frame-line: #c8c8c8;
    --map-blue: #7fcdee;
    --paper: #ffffff;
  }
  * { box-sizing: border-box; margin: 0; padding: 0; }
  html, body {
    width: 1200px; height: 1065px; overflow: hidden;
    background: var(--paper);
  }
  .canvas { position: relative; width: 1200px; height: 1065px; }

  .option-tag {
    position: absolute; left: 453px; top: 32px; width: 294px; height: 80px;
    background: #fff200; border-radius: 50%;
    display: flex; align-items: center; justify-content: center;
    font: 900 36px "Nunito Sans", sans-serif; color: var(--ink);
  }
  .option-note {
    position: absolute; left: 0; top: 124px; width: 1200px; text-align: center;
    font: 800 40px "Nunito Sans", sans-serif; color: var(--ink);
  }

  .advert {
    position: absolute; left: 24px; top: 209px; width: 1153px; height: 823px;
    border: 1px solid var(--frame-line); background: var(--paper); overflow: hidden;
  }

  .brand-mark {
    position: absolute; left: 76px; top: 110px; width: 230px; height: 230px;
    background: linear-gradient(135deg, #d2d3d5, #8e8f93);
  }
  .brand-name {
    position: absolute; left: 403px; top: 150px;
    font: 700 90px/1 "Montserrat", sans-serif; color: var(--brand-crimson);
    letter-spacing: -1px;
  }
  .tagline {
    position: absolute; left: 409px; top: 268px; width: 720px;
    font: 700 23px/41px "Merriweather", serif; color: var(--ink);
  }

  .web-band {
    position: absolute; left: 0; top: 372px; width: 100%; height: 154px;
    background: var(--band-yellow);
  }
  .web-band .home-icon { position: absolute; left: 16px; top: 54px; }
  .web-address {
    position: absolute; left: 128px; top: 22px;
    font: 800 80px/1.3 "Nunito Sans", sans-serif; color: var(--ink);
    letter-spacing: -0.5px;
  }
  .map-badge {
    position: absolute; left: 931px; top: 316px; width: 194px; height: 194px;
    border-radius: 50%; background: var(--band-yellow);
    display: flex; align-items: center; justify-content: center;
  }
  .map-badge .inner {
    width: 180px; height: 180px; border-radius: 50%; background: var(--paper);
    display: flex; align-items: center; justify-content: center;
  }
  .map-badge .map-art {
    width: 120px; height: 100px; border-radius: 4px;
    background: linear-gradient(135deg, var(--map-blue), #5e8fbf);
  }

  .selling-points {
    position: absolute; left: 336px; top: 563px; list-style: none;
    font: 400 20px/41px "Merriweather", serif; color: var(--ink);
  }
  .selling-points li { display: flex; align-items: center; gap: 22px; }
  .selling-points svg { flex: none; }
  .selling-points .brand-ref { color: var(--brand-crimson); }

  .join-panel {
    position: absolute; left: 0; top: 711px; width: 318px; height: 112px;
    background: var(--panel-grey); color: var(--paper);
    padding: 12px 0 0 31px;
    font: 700 20px/36px "Merriweather", serif;
  }
  .contact-email {
    position: absolute; left: 336px; top: 722px;
    display: flex; align-items: center; gap: 20px;
  }
  .contact-email span {
    font: 800 60px/1.3 "Nunito Sans", sans-serif; color: var(--ink);
  }
</style>
</head>
<body>
<div class="canvas">
  <div class="option-tag">OPTION-7</div>
  <div class="option-note">Font Changed</div>

  <section class="advert">
    <div class="brand-mark" aria-hidden="true"></div>
    <div class="brand-name">LOTWISEHUB</div>
    <p class="tagline">Australia's ONLY dedicated portal for permit approved development sites for sale.</p>

    <div class="web-band">
      <svg class="home-icon" width="68" height="56" viewBox="0 0 68 56" aria-hidden="true">
        <polygon points="34,2 2,28 10,28 10,54 58,54 58,28 66,28 54,18 54,6 47,6 47,12" fill="var(--ink)"/>
        <rect x="40" y="36" width="9" height="18" fill="var(--band-yellow)"/>
        <rect x="18" y="34" width="9" height="8" fill="var(--band-yellow)"/>
      </svg>
      <div class="web-address">lotwisehub.com.au</div>
    </div>

    <div class="map-badge">
      <div class="inner">
        <div class="map-art" role="img" aria-label="Illustration of a folded street map with route markers"></div>
      </div>
    </div>

    <ul class="selling-points">
      <li><svg width="16" height="12" viewBox="0 0 16 12"><polygon points="8,0 0,5 2,5 2,12 14,12 14,5 16,5" fill="var(--brand-crimson)"/><rect x="4" y="7" width="8" height="2" fill="#fff"/></svg><span><span class="brand-ref">Lotwise Hub</span> is at the forefront of market trends</span></li>
      <li><svg width="16" height="12" viewBox="0 0 16 12"><polygon points="8,0 0,5 2,5 2,12 14,12 14,5 16,5" fill="var(--brand-crimson)"/><rect x="4" y="7" width="8" height="2" fill="#fff"/></svg><span>Directly targeting the property developers and investors market</span></li>
      <li><svg width="16" height="12" viewBox="0 0 16 12"><polygon points="8,0 0,5 2,5 2,12 14,12 14,5 16,5" fill="var(--brand-crimson)"/><rect x="4" y="7" width="8" height="2" fill="#fff"/></svg><span>73% of Agencies have listed multiple properties</span></li>
    </ul>

    <div class="join-panel">Join Melbourne<br>Leading Agencies Today</div>

    <div class="contact-email">
      <svg width="40" height="28" viewBox="0 0 40 28" aria-hidden="true">
        <rect x="0" y="0" width="40" height="28" fill="var(--ink)"/>
        <polyline points="1,1 20,16 39,1" fill="none" stroke="#fff" stroke-width="2.5"/>
        <line x1="1" y1="27" x2="15" y2="12" stroke="#fff" stroke-width="2"/>
        <line x1="39" y1="27" x2="25" y2="12" stroke="#fff" stroke-width="2"/>
      </svg>
      <span>info@lotwisehub.com.au</span>
    </div>
  </section>
</div>
</body>
</html>
```